Kitchen manufaturer business card/logo design

I am a small kitchen manufacturing company that makes and installs all sorts of cabinetry.

The colours im looking to incorporate in the card are light/baby blue, white and black.

Incorporate 5 stars to show quality workmanship and product.

Looking for a modern classy design.
Updates

Hey guys, New idea. The logo should be made using HK in the most modern way possible as well as the full company name below it. Thanks.

Target Market(s)

Anyone with a home thats looking for a new cabinetry of any sort.

Industry/Entity Type

Business

Contact Information for Business Card

Harbor Kitchens
Ted Lowther
PH 0491 358 902
Email- harborkitchens@mailvane.example
ABN- 83 507 962 318
-Kitchens
-Vanities
-Laundries
-Media Units
-Studies
-Wardrobes
-3D Computer Designs

Requirements
Must have

• The front of the card must only have the company name.
The different types of cabinetry I do must be on the back of the card in point form but instead of using points use stars.
Nice to have
• Just think classy and quality

```html
<!DOCTYPE html>
<html lang="en">
<head>
<meta charset="utf-8">
<title>Harbor Kitchens — Business Card</title>
<link rel="stylesheet" href="https://fonts.googleapis.com/css2?family=Open+Sans:wght@400;700&display=swap">
<style>
  :root {
    --sky: #7dcfea;
    --ink: #1e1f21;
    --paper: #ffffff;
    --backdrop: #e4e5e7;
    --text-dark: #2c2d30;
    --text-mid: #4a4b4f;
  }
  * { margin: 0; padding: 0; box-sizing: border-box; }
  html, body {
    width: 1200px; height: 1200px; overflow: hidden;
    background: var(--backdrop);
    font-family: "Open Sans", sans-serif;
  }
  .card {
    position: absolute; left: 180px; width: 840px; height: 480px;
    overflow: hidden;
    box-shadow: 0 6px 18px rgba(0,0,0,0.12);
  }
  .card--front { top: 80px; background: var(--ink); }
  .card--back  { top: 640px; background: var(--paper); }
  .card svg.frame { position: absolute; inset: 0; }

  .front-name {
    position: absolute; left: 250px; top: 190px; width: 340px;
    text-align: center;
    color: var(--paper); font-weight: 700; font-size: 30px; letter-spacing: 1px;
    text-transform: uppercase;
  }
  .front-name .mark-square {
    display: block; width: 46px; height: 46px; margin: 0 auto 14px;
    background: var(--sky);
  }

  .back-name {
    position: absolute; left: 540px; top: 110px; width: 250px;
    display: flex; align-items: center; gap: 12px;
    color: var(--text-dark); font-weight: 700; font-size: 22px; text-transform: uppercase;
    letter-spacing: 0.5px;
  }
  .back-name .mark-square { width: 34px; height: 34px; background: var(--sky); flex: none; }

  .person {
    position: absolute; left: 40px; top: 250px; width: 300px; text-align: right;
    color: var(--text-dark);
  }
  .person__name { font-weight: 700; font-size: 25px; line-height: 30px; }
  .person__abn { font-size: 19px; line-height: 24px; color: var(--text-mid); }

  .contact {
    position: absolute; left: 356px; top: 256px; font-size: 21px; line-height: 28px;
    color: var(--text-dark);
  }
  .contact__row { display: flex; align-items: center; gap: 10px; }
  .contact__row svg { flex: none; }

  .services {
    position: absolute; left: 70px; top: 330px; font-size: 19px; line-height: 30px;
    color: var(--text-mid); list-style: none;
  }
  .services li { display: inline; margin-right: 6px; }
  .services .star { color: var(--sky); margin-right: 4px; }
</style>
</head>
<body>

<section class="card card--front" aria-label="Card front">
  <svg class="frame" width="840" height="480" viewBox="0 0 840 480">
    <g stroke="#7dcfea" stroke-width="1.5" fill="none">
      <line x1="0" y1="150" x2="840" y2="150"/>
      <line x1="200" y1="150" x2="200" y2="480"/>
      <line x1="560" y1="0" x2="560" y2="480"/>
      <line x1="740" y1="0" x2="740" y2="480"/>
      <line x1="560" y1="300" x2="840" y2="300"/>
    </g>
    <rect x="20" y="200" width="170" height="150" fill="#7dcfea"/>
    <rect x="580" y="160" width="150" height="130" fill="#7dcfea"/>
  </svg>
  <div class="front-name"><span class="mark-square"></span>Harbor Kitchens</div>
</section>

<section class="card card--back" aria-label="Card back">
  <svg class="frame" width="840" height="480" viewBox="0 0 840 480">
    <g stroke="#7dcfea" stroke-width="1.5" fill="none">
      <line x1="520" y1="80" x2="840" y2="80"/>
      <line x1="520" y1="80" x2="520" y2="310"/>
      <line x1="340" y1="420" x2="840" y2="420"/>
    </g>
    <rect x="520" y="170" width="300" height="18" fill="#7dcfea"/>
    <rect x="0" y="244" width="346" height="66" fill="#7dcfea"/>
  </svg>

  <div class="back-name"><span class="mark-square"></span>Harbor Kitchens</div>

  <div class="person">
    <p class="person__name">Ted Lowther</p>
    <p class="person__abn">ABN-83 507 962 318</p>
  </div>

  <div class="contact">
    <p class="contact__row">
      <svg width="18" height="20" viewBox="0 0 18 20" aria-hidden="true">
        <rect x="2" y="1" width="14" height="18" rx="2" fill="#2c2d30"/>
        <rect x="5" y="4" width="8" height="6" fill="#fff"/>
      </svg>
      0491 358 902
    </p>
    <p class="contact__row">
      <svg width="18" height="14" viewBox="0 0 18 14" aria-hidden="true">
        <rect x="1" y="1" width="16" height="12" fill="#2c2d30"/>
        <polyline points="1,1 9,8 17,1" fill="none" stroke="#fff" stroke-width="1.5"/>
      </svg>
      harborkitchens@mailvane.example
    </p>
  </div>

  <ul class="services">
    <li><span class="star">★</span>Kitchens</li>
    <li><span class="star">★</span>Vanities</li>
    <li><span class="star">★</span>Laundries</li>
    <li><span class="star">★</span>Media Units</li>
    <br>
    <li><span class="star">★</span>Studies</li>
    <li><span class="star">★</span>Wardrobes</li>
    <li><span class="star">★</span>3D Computer Designs</li>
  </ul>
</section>

</body>
</html>
```